Fire Risk Assessment App needs a sleek UI design

I need a sleek, modern but professional design for my 5 page Fire Risk Assessment App. Include gradient background, fire themed colours including reds, yellows, light orange and a touch of black. Design must ooze simplicity and professionalism. This is for the UK market. See attached images and word doc for more information.

Target Market(s)

General public and business owners

Industry/Entity Type

Technology / Fire Safety

Colors
00AB8E
00BBA5
67D7C9
C6EFE9
E9F9F6
59FF00
82FF00
B8FF75
E3FFCB
F4FFEA
FFC000
F8CF3A
FAE287
FDF2CF
FEFAEE
F0912C
F2A743
F7CA91
FBE8D2
FDF5EE
EE7325
F08F49
F5BC92
FAE3D3
FDF4ED
EB3D1F
EC4F4E
F09395
F8D3D4
FCEDEE

```html
<!DOCTYPE html>
<html lang="en">
<head>
<meta charset="utf-8">
<title>Fire Risk Assessment App – Screens</title>
<link href="https://fonts.googleapis.com/css2?family=Lato:wght@400;700&display=swap" rel="stylesheet">
<style>
:root{
  --page:#dfe0e6;
  --screen-top:#fdf5f3;
  --screen-bottom:#f3dadb;
  --accent:#ff5733;
  --accent-soft:#f4a394;
  --ink:#2a2a2a;
  --muted:#6a6a6a;
  --field-line:#f1a89a;
  --rule:#d9c3c3;
  --green:#2ebd59;
  --slate:#7f93a6;
  --nav:#444;
}
*{box-sizing:border-box;margin:0;padding:0}
html,body{width:1200px;height:1124px;overflow:hidden}
body{background:var(--page);font-family:'Lato',sans-serif;color:var(--ink);position:relative}
.screen{position:absolute;width:219px;height:478px;border-radius:30px;overflow:hidden;
  background:linear-gradient(180deg,var(--screen-top) 0%,var(--screen-bottom) 100%);
  box-shadow:0 10px 30px rgba(60,60,80,.18)}
.screen > *{position:absolute}
.title{left:0;right:0;top:39px;text-align:center;font-size:11.5px;font-weight:700;letter-spacing:.2px}
.title-icon{left:20px;top:40px;width:12px;height:12px}
.hero{background:radial-gradient(circle at 50% 45%,#ffffff 0%,#e9e4e4 55%,rgba(233,228,228,0) 75%)}
.center-text{left:0;right:0;text-align:center;font-size:8.5px}
.field{left:20px;width:179px;height:39px;border:1px solid var(--field-line);font-size:10px;padding:0 11px;display:flex;align-items:center}
.field.stack{flex-direction:column;align-items:flex-start;justify-content:center;padding-left:10px}
.field .label{font-size:8.5px}
.field .value{font-size:10px;margin-top:4px}
.field .hint{font-size:10px;margin-top:4px;color:#9a9a9a}
.field.choice{height:67px;flex-direction:column;align-items:flex-start;justify-content:center;gap:6px;padding-left:10px}
.choice .opt{display:flex;align-items:center;gap:6px;color:var(--muted);font-size:10px}
.box{width:10px;height:10px;border:1px solid #e9695c;border-radius:2px}
.btn{left:20px;width:179px;height:39px;background:var(--accent);color:#fff;font-size:10px;display:flex;align-items:center;justify-content:center;box-shadow:0 3px 8px rgba(255,87,51,.35)}
.link{color:var(--accent);font-weight:700}
/* dashboard */
.round{border-radius:50%;display:flex;align-items:center;justify-content:center}
.cap{font-size:7.5px;text-align:center;width:60px}
.section{left:20px;width:179px;font-size:9.5px;font-weight:700;display:flex;justify-content:space-between;align-items:center}
.rule{left:20px;width:179px;height:1px;background:var(--rule)}
.item{left:26px;font-size:7.5px;display:flex;align-items:center;gap:7px}
.dot{width:5px;height:5px;border-radius:50%;background:var(--accent)}
/* nav */
.nav{left:0;right:0;top:441px;height:37px;border-top:1px solid var(--rule);display:flex;justify-content:space-around;align-items:center;padding:0 16px 4px}
.nav svg{width:12px;height:12px;stroke:var(--nav);fill:none;stroke-width:1.8}
.nav svg.on{stroke:var(--accent)}
/* questions */
.qhead{left:20px;font-size:7.8px;line-height:12.3px;top:60px}
.qno{left:20px;top:180px;font-size:10px;font-weight:700}
.qtext{left:20px;top:201px;width:180px;font-size:7.6px;line-height:13.5px}
.note{left:20px;width:179px;border:1px solid var(--field-line);font-size:7.5px;display:flex;align-items:center}
.small-btn{font-size:7.5px;height:16px;display:flex;align-items:center;justify-content:center}
/* payment */
.price-row{left:20px;width:180px;height:12px;font-size:7.6px;font-weight:700}
.price-row span{position:absolute;top:0}
.tag{background:#f0533a;color:#fde;text-decoration:line-through;font-weight:400;padding-left:4px;width:45px;height:12px;line-height:12px;clip-path:polygon(0 0,100% 0,86% 50%,100% 100%,0 100%)}
</style>
</head>
<body>

<!-- Welcome -->
<section class="screen" style="left:97px;top:69px">
  <div class="hero" role="img" aria-label="Illustration of stacked assessment reports with charts" style="left:51px;top:48px;width:97px;height:106px"></div>
  <p class="center-text" style="top:176px">Quick tap response and voice activated typing.</p>
  <div class="btn" style="left:45px;top:212px;width:128px;flex-direction:column;gap:3px">
    <svg width="11" height="11" viewBox="0 0 24 24" fill="none" stroke="#fff" stroke-width="1.8"><circle cx="12" cy="12" r="10"/><circle cx="12" cy="10" r="3"/><path d="M6.5 18.5c1.5-2.5 9.5-2.5 11 0"/></svg>
    Customer Login</div>
  <p class="center-text" style="top:277px">Any Responsible Person can do it.</p>
  <div class="field" style="left:45px;top:314px;width:128px;height:38px;flex-direction:column;justify-content:center;gap:3px;padding:0">
    <svg width="11" height="11" viewBox="0 0 24 24" fill="none" stroke="var(--accent)" stroke-width="1.8"><circle cx="10" cy="8" r="4"/><path d="M3 20c1-4 13-4 14 0M19 8v6M16 11h6"/></svg>
    Create a Free Account</div>
  <p class="center-text" style="top:424px">Create and endorsed by British Firefighters.</p>
</section>

<!-- Login -->
<section class="screen" style="left:360px;top:69px">
  <h1 class="title">LOGIN</h1>
  <div class="hero" role="img" aria-label="Illustration of stacked assessment reports with charts" style="left:72px;top:61px;width:72px;height:75px"></div>
  <div class="field" style="top:149px">Email</div>
  <div class="field" style="top:199px">Password</div>
  <div class="btn" style="top:254px">Login</div>
  <p class="center-text" style="top:308px">Forgot password?</p>
  <p class="center-text" style="top:334px">Don't have an acount?</p>
  <p class="center-text link" style="top:359px">Sign Up</p>
</section>

<!-- Sign up 1 -->
<section class="screen" style="left:623px;top:69px">
  <h1 class="title">SIGN UP</h1>
  <div class="hero" role="img" aria-label="Illustration of stacked assessment reports with charts" style="left:72px;top:61px;width:72px;height:75px"></div>
  <div class="field" style="top:149px">Name</div>
  <div class="field" style="top:199px">Email</div>
  <div class="field" style="top:248px">Password</div>
  <div class="field stack" style="top:296px"><span class="label">Country</span><span class="value">United Kingdom</span></div>
  <div class="field stack" style="top:345px"><span class="label">Mobile Number</span><span class="hint">+44</span></div>
  <div class="field choice" style="top:394px"><span>I am a</span>
    <span class="opt"><i class="box"></i>Fire Risk Assessor</span>
    <span class="opt"><i class="box"></i>Premises Owner</span></div>
</section>

<!-- Sign up 2 -->
<section class="screen" style="left:887px;top:69px">
  <h1 class="title">SIGN UP</h1>
  <div class="field" style="top:89px">Email</div>
  <div class="field" style="top:138px">Password</div>
  <div class="field stack" style="top:187px"><span class="label">Country</span><span class="value">United Kingdom</span></div>
  <div class="field stack" style="top:236px"><span class="label">Mobile Number</span><span class="hint">+44</span></div>
  <div class="field choice" style="top:285px"><span>I am a</span>
    <span class="opt"><i class="box"></i>Fire Risk Assessor</span>
    <span class="opt"><i class="box"></i>Premises Owner</span></div>
  <div class="btn" style="top:369px">Sign Up</div>
  <p class="center-text" style="top:426px">Already have an account?</p>
  <p class="center-text link" style="top:451px">Login</p>
</section>

<!-- Dashboard -->
<section class="screen" style="left:97px;top:579px">
  <svg class="title-icon" viewBox="0 0 24 24" fill="none" stroke="var(--accent)" stroke-width="2"><path d="M3 17a9 9 0 1 1 18 0"/><path d="M12 17l4-5"/></svg>
  <h1 class="title">DASHBOARD</h1>
  <div class="round" style="left:92px;top:63px;width:34px;height:34px;background:var(--accent)">
    <svg width="18" height="18" viewBox="0 0 18 18"><path d="M6.5 1h5v5.5H17v5h-5.5V17h-5v-5.5H1v-5h5.5z" fill="#fff"/></svg></div>
  <div class="round" style="left:59px;top:96px;width:32px;height:32px;background:var(--slate)">
    <svg width="16" height="16" viewBox="0 0 24 24" fill="none" stroke="#fff" stroke-width="1.6"><path d="M3 11l9-7 9 7v9H3z"/><path d="M10 20v-6h4v6"/></svg></div>
  <div class="round" style="left:126px;top:96px;width:32px;height:32px;background:var(--slate)">
    <svg width="16" height="16" viewBox="0 0 24 24" fill="none" stroke="#fff" stroke-width="1.6"><rect x="5" y="4" width="14" height="16"/><path d="M9 8h2M13 8h2M9 12h2M13 12h2M10 20v-4h4v4"/></svg></div>
  <span class="cap" style="left:45px;top:131px">Residential</span>
  <span class="cap" style="left:112px;top:131px">Commercial</span>

  <div class="section" style="top:167px">COMPLETE
    <svg width="12" height="12" viewBox="0 0 24 24" fill="none" stroke="var(--accent)" stroke-width="2"><path d="M21 12a9 9 0 1 1-4-7.5"/><path d="M8 12l3 3 9-9"/></svg></div>
  <div class="rule" style="top:185px"></div>
  <div class="item" style="top:193px"><svg width="9" height="6" viewBox="0 0 18 12" fill="none" stroke="var(--accent-soft)" stroke-width="2"><path d="M0 6h15M10 1l5 5-5 5"/></svg>ELM STREET BARBERS</div>
  <div class="item" style="top:214px"><svg width="9" height="6" viewBox="0 0 18 12" fill="none" stroke="var(--accent-soft)" stroke-width="2"><path d="M0 6h15M10 1l5 5-5 5"/></svg>RIVERSIDE KITCHEN</div>

  <div class="section" style="top:266px">INPROGRESS
    <svg width="12" height="12" viewBox="0 0 24 24" fill="none" stroke="var(--accent)" stroke-width="2"><circle cx="12" cy="12" r="9"/><circle cx="12" cy="12" r="4"/><path d="M5.5 5.5l3.7 3.7M18.5 5.5l-3.7 3.7M5.5 18.5l3.7-3.7M18.5 18.5l-3.7-3.7"/></svg></div>
  <div class="rule" style="top:284px"></div>
  <div class="item" style="left:23px;top:293px"><i class="dot"></i>OAKFIELD SCHOOL</div>
  <div class="item" style="left:23px;top:312px"><i class="dot"></i>BEECHWOOD CARE HOME</div>

  <div class="section" style="top:357px">PURCHASES
    <svg width="12" height="12" viewBox="0 0 24 24" fill="none" stroke="var(--accent)" stroke-width="2"><path d="M4 8h16l-1 13H5z"/><path d="M8 8V6a4 4 0 0 1 8 0v2"/></svg></div>
  <div class="rule" style="top:375px"></div>
  <div class="item" style="left:23px;top:384px"><i class="dot"></i>RESIDENTIAL FIRE RISK ASSESSMENT</div>
  <div class="item" style="left:23px;top:402px"><i class="dot"></i>COMMERCIAL FIRE RISK ASSESSMENT</div>
  <div class="item" style="left:23px;top:421px"><i class="dot"></i>COMMERCIAL FIRE RISK ASSESSMENT</div>

  <nav class="nav">
    <svg class="on" viewBox="0 0 24 24"><path d="M3 17a9 9 0 1 1 18 0"/><path d="M12 17l4-5"/></svg>
    <svg viewBox="0 0 24 24"><rect x="3" y="5" width="18" height="14" rx="2"/><path d="M3 10h18"/></svg>
    <svg viewBox="0 0 24 24"><path d="M4 4h16v12H9l-5 4z"/><path d="M8 9h8M8 12h6"/></svg>
    <svg viewBox="0 0 24 24"><path d="M15 5.5A8 8 0 1 0 15 18.5"/><path d="M10 12h11M17 8l4 4-4 4"/></svg>
  </nav>
</section>

<!-- Questions -->
<section class="screen" style="left:360px;top:579px">
  <svg class="title-icon" viewBox="0 0 24 24" fill="none" stroke="var(--accent)" stroke-width="2"><path d="M3 17a9 9 0 1 1 18 0"/><path d="M12 17l4-5"/></svg>
  <h1 class="title">QUESTIONS</h1>
  <p class="qhead">FIRE RISK ASSESSMENT<br>FIRE HAZARD<br>SETION : 7.0 / 30.00<br>ELECTRONIC SOURCE OF IGNITION<br>( CLAUSE 13 &amp; ANNE&nbsp; X B)</p>
  <svg style="left:172px;top:64px" width="28" height="58" viewBox="0 0 28 58" fill="none" stroke-width="3">
    <circle cx="14" cy="13" r="11" stroke="#e6e2e2"/><path d="M14 2a11 11 0 1 1-10 6" stroke="var(--green)"/>
    <circle cx="14" cy="44" r="11" stroke="#e6e2e2"/><path d="M14 33a11 11 0 1 1-11 11" stroke="var(--green)"/>
  </svg>
  <div class="round" style="left:93px;top:129px;width:32px;height:32px;background:#fff;box-shadow:0 2px 6px rgba(0,0,0,.08)">
    <svg width="22" height="22" viewBox="0 0 24 24" fill="none"><circle cx="12" cy="12" r="10" stroke="#444" stroke-width="1.4"/><path d="M13 4L7 13h5l-1 7 6-9h-5z" fill="#ffc000"/></svg></div>
  <p class="qno">Q : 7.01</p>
  <div class="rule" style="top:197px"></div>
  <p class="qtext">Are reasonable measures taken to prevent fires of electrical origin?</p>
  <svg style="left:42px;top:234px" width="136" height="14" viewBox="0 0 136 14" fill="none" stroke-width="1.3">
    <circle cx="7" cy="7" r="5.5" stroke="var(--green)"/><path d="M4.5 7l2 2 3-3.5" stroke="var(--green)"/>
    <circle cx="37" cy="7" r="5.5" stroke="var(--accent)"/><path d="M35 5l4 4M39 5l-4 4" stroke="var(--accent)"/>
    <circle cx="67" cy="7" r="5.5" stroke="#f7a541"/><path d="M64.5 7h5" stroke="#f7a541"/>
    <path d="M92 4.5h2l1-1.5h4l1 1.5h2v7h-10z" stroke="#333"/><circle cx="97" cy="8" r="2" stroke="#333"/>
    <rect x="125" y="1.5" width="4" height="7" rx="2" stroke="#333"/><path d="M123 7a4 4 0 0 0 8 0M127 11v2" stroke="#333"/>
  </svg>
  <div class="note" style="top:261px;height:39px;padding-left:11px">Reason Goes Here....</div>
  <div class="note" style="top:314px;height:77px;justify-content:center">Picture Here</div>
  <div class="small-btn" style="left:20px;top:412px;width:52px;border:1px solid #cbbcbc">Save &amp; Close</div>
  <div class="small-btn" style="left:143px;top:412px;width:56px;background:var(--accent);color:#fff;gap:6px">Next
    <svg width="7" height="7" viewBox="0 0 12 12" fill="none" stroke="#fff" stroke-width="1.8"><path d="M1 1l5 5-5 5M6 1l5 5-5 5"/></svg></div>
  <nav class="nav">
    <svg class="on" viewBox="0 0 24 24"><path d="M3 17a9 9 0 1 1 18 0"/><path d="M12 17l4-5"/></svg>
    <svg viewBox="0 0 24 24"><rect x="3" y="5" width="18" height="14" rx="2"/><path d="M3 10h18"/></svg>
    <svg viewBox="0 0 24 24"><path d="M4 4h16v12H9l-5 4z"/><path d="M8 9h8M8 12h6"/></svg>
    <svg viewBox="0 0 24 24"><path d="M15 5.5A8 8 0 1 0 15 18.5"/><path d="M10 12h11M17 8l4 4-4 4"/></svg>
  </nav>
</section>

<!-- Payment -->
<section class="screen" style="left:623px;top:579px">
  <svg class="title-icon" viewBox="0 0 24 24" fill="none" stroke="var(--accent)" stroke-width="2"><rect x="3" y="5" width="18" height="14" rx="2"/><path d="M3 10h18"/></svg>
  <h1 class="title">PAYMENT</h1>
  <p class="center-text" style="top:135px;font-size:7.6px;font-weight:700;line-height:12px">FIRE RISK ASSESSMENT<br>PAYMENT OPTIONS</p>
  <div class="price-row" style="top:180px"><span style="left:0">BRONZE&nbsp;&nbsp; 1</span><span style="left:72px">-</span><span style="left:93px">£ 19.99</span></div>
  <div class="price-row" style="top:203px"><span style="left:0">SILVER&nbsp;&nbsp; 3</span><span style="left:72px">-</span><span style="left:93px">£ 54.99</span><span class="tag" style="left:134px">£ 59.97</span></div>
  <div class="price-row" style="top:227px"><span style="left:0">GOLD&nbsp;&nbsp; 5</span><span style="left:72px">-</span><span style="left:93px">£ 89.99</span><span class="tag" style="left:134px">£ 99.95</span></div>
  <div class="price-row" style="top:251px"><span style="left:0">PLATINUM&nbsp;&nbsp; 10</span><span style="left:72px">-</span><span style="left:93px">£ 174.99</span><span class="tag" style="left:134px">£ 199.90</span></div>
  <nav class="nav">
    <svg viewBox="0 0 24 24"><path d="M3 17a9 9 0 1 1 18 0"/><path d="M12 17l4-5"/></svg>
    <svg class="on" viewBox="0 0 24 24"><rect x="3" y="5" width="18" height="14" rx="2"/><path d="M3 10h18"/></svg>
    <svg viewBox="0 0 24 24"><path d="M4 4h16v12H9l-5 4z"/><path d="M8 9h8M8 12h6"/></svg>
    <svg viewBox="0 0 24 24"><path d="M15 5.5A8 8 0 1 0 15 18.5"/><path d="M10 12h11M17 8l4 4-4 4"/></svg>
  </nav>
</section>

<!-- Technical support -->
<section class="screen" style="left:887px;top:579px">
  <svg class="title-icon" viewBox="0 0 24 24" fill="none" stroke="var(--accent)" stroke-width="2"><path d="M4 4h16v12H9l-5 4z"/><path d="M8 9h8M8 12h6"/></svg>
  <h1 class="title">TECHNICAL SUPPORT</h1>
  <p class="center-text" style="top:62px;font-size:7.6px;font-weight:700">Type / Record your response here</p>
  <svg style="left:188px;top:77px" width="11" height="12" viewBox="0 0 12 14" fill="none" stroke="var(--slate)" stroke-width="1.2"><rect x="4" y="1" width="4" height="7" rx="2"/><path d="M2 7a4 4 0 0 0 8 0M6 11v2"/></svg>
  <div class="note" style="top:93px;height:77px;justify-content:center">Result Here</div>
  <div class="small-btn" style="left:155px;top:184px;width:44px;height:15px;background:var(--accent);color:#fff">SEND</div>
  <nav class="nav">
    <svg viewBox="0 0 24 24"><path d="M3 17a9 9 0 1 1 18 0"/><path d="M12 17l4-5"/></svg>
    <svg viewBox="0 0 24 24"><rect x="3" y="5" width="18" height="14" rx="2"/><path d="M3 10h18"/></svg>
    <svg class="on" viewBox="0 0 24 24"><path d="M4 4h16v12H9l-5 4z"/><path d="M8 9h8M8 12h6"/></svg>
    <svg viewBox="0 0 24 24"><path d="M15 5.5A8 8 0 1 0 15 18.5"/><path d="M10 12h11M17 8l4 4-4 4"/></svg>
  </nav>
</section>

</body>
</html>
```